Responsive WordPress website for medical therapy practice consulting business.

We need both design and website for responsive Wordpress website. The use of Quorvel theme is preferred when considering the design (not required).
Site must be designed for 1920px width and fully responsive.
See full scope of the project below.

DESIGN:
Design a full screen layout using images and parallax movement where appropriate.
Easy to use navigation for desktop and hamburger style navigation for mobile devices.
Create an original design for the home, sub-page template.
Create a responsive website using common desktop breakpoints 1920, 1366, 1280 1024 as well as mobile devices.
Color scheme should use soft or pastel color avoiding reds.
Design will take inspiration from logo design and color scheme.
Large “Hero slider” may be employed to striking visual interest.
The website will focus the content on the Homepage mission statement, What We Do and How to Reach Us, content.
Website Footer Information: Include content for Privacy Policy and Terms of Use, address and copyright information.

DEVELOPMENT NOTES:

WordPress content management platform will be used .

Responsive grid will be used to properly display website content on all devices including mobile, laptop and desktop at standard breakpoints.

Social Media links to LinkedIn and Twitter

Google Analytics and Search Console integration – allows tracking of visitors and in-depth search data, indexing and performance.

Yoast Basic SEO – basic setup and integration is included in the proposal. This includes creating SEO friendly page titles, search descriptions and best practices for heading and image tags.

508 & ADA compliance

PAGE LIST:
The following pages are a list of current websites pages. These are used as a guideline for developing the proposal and can be changed to reflect content:

NAVIGATION LINKS:

HOME

· Featuring the new logo, the home page will display Brightmoor Care Partners’s message, services, and contact information.
· The navigation will be prominent, intuitive and easy to use, allowing to find information quickly.
· Parallax scrolling will provide a cool modern visual effect without being overbearing.

====================================================

ABOUT US –

· History
· Bios
· Links

SERVICES

· Business Consultancy service

CONTACT US – This section will present ways for viewers to reach out either by phone, email.

· Google map of office locations.
· Business information
a. Locations
b. Address
c. Phone
d. Fax
e. Email

FOOTER LINKS – Additional information for legal or usage claims, company info and contact info.

· Copyright information
· Links to CONTACT
· Social Media
· Disclaimer
· Privacy policy
· Terms of use

```html
<!DOCTYPE html>
<html lang="en">
<head>
<meta charset="utf-8">
<title>Brightmoor Care Partners</title>
<link href="https://fonts.googleapis.com/css2?family=Raleway:wght@400;500;600;700&display=swap" rel="stylesheet">
<style>
:root{
  --blue:#1f8ad6;
  --blue-dark:#1565b0;
  --navy:#1b3d72;
  --ink:#222;
  --grey:#777;
  --line:#dcdcdc;
  --light-text:#f2f2f2;
  --white:#fff;
}
*{box-sizing:border-box;margin:0;padding:0}
html,body{width:1200px;height:4054px;overflow:hidden;background:var(--white);font-family:'Raleway',sans-serif;color:var(--ink)}
.page{position:relative;width:1200px;height:4054px}
.abs{position:absolute}
/* header */
.topbar{left:700px;top:0;width:500px;height:46px;background:var(--blue);color:#fff;font-size:13px;display:flex;align-items:center;gap:26px;padding-left:40px;clip-path:polygon(4% 0,100% 0,100% 100%,0 100%)}
.brand{left:128px;top:34px;display:flex;align-items:center;gap:12px;font-size:30px;font-weight:700;color:var(--navy)}
.brand .dot{width:26px;height:26px;border-radius:50%;background:var(--blue)}
.nav{left:540px;top:80px;display:flex;gap:34px;font-size:16px;color:var(--ink)}
/* hero */
.hero{left:0;top:120px;width:1200px;height:640px;background:linear-gradient(100deg,#9d8373 0%,#c9b8aa 45%,#e9e3dc 100%)}
.hero-title{left:127px;top:248px;font-size:42px;font-weight:500;color:var(--white);line-height:58px;letter-spacing:.5px;text-shadow:0 1px 3px rgba(0,0,0,.25)}
.hero-title b{font-weight:600}
.hero-sub{left:130px;top:372px;font-size:26px;font-weight:600;color:var(--white);line-height:38px;text-shadow:0 1px 3px rgba(0,0,0,.25)}
.btn{background:var(--blue);color:#fff;display:flex;align-items:center;justify-content:center;font-weight:600}
.hero-btn{left:127px;top:465px;width:196px;height:56px;font-size:22px}
/* about */
.h2{width:1200px;left:0;text-align:center;font-size:40px;font-weight:500;color:var(--blue)}
.h2 b{font-weight:700}
.h3{font-size:32px;font-weight:500;color:var(--ink)}
.para{font-size:14px;line-height:28px;color:var(--grey)}
.photo{border-radius:50%;border:10px solid var(--navy)}
.small-btn{left:600px;top:1522px;width:110px;height:34px;font-size:13px}
/* services */
.services{left:0;top:1650px;width:1200px;height:760px;background:linear-gradient(120deg,#3a3a3d,#2a2a2c 60%,#4b4845)}
.services-text{color:var(--light-text);text-align:justify}
/* contact info */
.info{width:300px;text-align:center;font-size:19px;line-height:30px;color:#333}
.info .icon{width:96px;height:96px;border-radius:50%;background:var(--blue);margin:0 auto 18px;display:flex;align-items:center;justify-content:center}
/* map */
.map{left:0;top:2690px;width:1200px;height:380px;background:linear-gradient(135deg,#e7eee5,#dfe6ee 50%,#ece9e1)}
.card{left:215px;width:495px;padding:14px 70px;font-size:14px;line-height:26px;background:#fff;color:#333;box-shadow:0 2px 8px rgba(0,0,0,.15)}
.card.active{background:var(--blue);color:#fff;font-weight:600}
.card p{display:flex;align-items:center;gap:12px}
/* form */
.field{height:50px;border-bottom:1px solid var(--line);border-left:1px solid var(--line);font-size:14px;color:#555;padding:14px 20px}
.submit{left:505px;top:3430px;width:190px;height:54px;font-size:20px}
/* footer */
.footer{left:0;top:3560px;width:1200px;height:494px;background:linear-gradient(180deg,#2f2f31,#1f1f20)}
.fcol{color:#fff;font-size:12px;line-height:22px}
.fcol h4{font-size:18px;font-weight:600;margin-bottom:14px;letter-spacing:.5px}
.copy{left:0;top:3988px;width:1200px;text-align:center;color:#ddd;font-size:12px}
</style>
</head>
<body>
<div class="page">

  <header>
    <div class="abs topbar"><span>&#9742; Phone: 555 014 2290</span><span>&#9993; Mail: hello@brightmoorcare.net</span></div>
    <div class="abs brand"><span class="dot"></span>Brightmoor Care Partners</div>
    <nav class="abs nav"><span>Home</span><span>About Brightmoor Care Partners</span><span>Our Services</span><span>Contact Us</span></nav>
  </header>

  <section>
    <div class="abs hero" role="img" aria-label="Photo of a therapist taking notes during a session"></div>
    <svg class="abs" style="left:0;top:580px" width="1200" height="280" viewBox="0 0 1200 280">
      <path d="M0 175 C320 40 760 10 1200 100 L1200 130 C760 40 320 70 0 190Z" fill="var(--blue)"/>
      <path d="M500 90 C780 40 1000 80 1200 170 L1200 280 C1030 150 800 90 500 90Z" fill="var(--blue-dark)"/>
      <path d="M0 190 C320 70 760 40 1200 130 L1200 280 L0 280Z" fill="#fff"/>
    </svg>
    <h1 class="abs hero-title"><b>WELCOME TO BRIGHTMOOR</b><br>CARE PARTNERS</h1>
    <p class="abs hero-sub">Sed ut perspiciatis unde omnis iste<br>natus error sit voluptatem accusantium</p>
    <div class="abs btn hero-btn">Read More</div>
  </section>

  <section>
    <h2 class="abs h2" style="top:855px">ABOUT US</h2>
    <h3 class="abs h3" style="left:0;width:1200px;text-align:center;top:908px">HISTORY</h3>
    <p class="abs para" style="left:180px;top:958px;width:840px;text-align:center">At vero eos et accusamus et iusto odio dignissimos ducimus qui blanditiis praesentium voluptatum deleniti atque corrupti quos dolores et quas molestias excepturi sint occaecati cupiditate non provident, similique sunt in culpa qui officia deserunt mollitia animi, id est laborum et dolorum fuga. Et harum quidem rerum facilis est et expedita distinctio. Nam libero tempore, cum soluta nobis est eligendi optio cumque nihil impedit quo minus id quod maxime placeat facere possimus, omnis voluptas assumenda est, omnis dolor repellendus. Temporibus autem quibusdam et aut officiis debitis aut rerum necessitatibus saepe eveniet ut et voluptates repudiandae sint et molestiae non recusandae.</p>
    <div class="abs photo" role="img" aria-label="Photo of a smiling client in a group therapy circle" style="left:118px;top:1145px;width:430px;height:430px;background:linear-gradient(135deg,#a9c3d6,#dfe5ea 60%,#c7b8a8)"></div>
    <h3 class="abs h3" style="left:598px;top:1182px;font-size:30px">BIO'S</h3>
    <p class="abs para" style="left:600px;top:1228px;width:478px;text-align:justify">At vero eos et accusamus et iusto odio dignissimos ducimus qui blanditiis praesentium voluptatum deleniti atque corrupti quos dolores et quas molestias excepturi sint occaecati cupiditate non provident, similique sunt in culpa qui officia deserunt mollitia animi, id est laborum et dolorum fuga. At vero eos et accusamus et iusto odio dignissimos ducimus qui blanditiis praesentium voluptatum deleniti atque corrupti quos dolores et quas molestias excepturi sint occaecati cupiditate non provident, similique sunt in culpa qui officia deserunt mollitia animi, id est laborum et dolorum fuga. Et harum quidem rerum facilis est et expedita distinctio.</p>
    <div class="abs btn small-btn">Read More</div>
  </section>

  <section>
    <div class="abs services" role="img" aria-label="Dark photo of a counselling office with a notebook"></div>
    <svg class="abs" style="left:0;top:1640px" width="1200" height="90" viewBox="0 0 1200 90">
      <path d="M0 0 L1200 0 L1200 60 C800 0 400 10 0 40Z" fill="#fff"/>
      <path d="M0 40 C400 10 800 0 1200 60 L1200 72 C800 14 400 26 0 48Z" fill="var(--navy)"/>
    </svg>
    <h2 class="abs h2" style="top:1825px;color:#fff;font-weight:400"><b>OUR</b> SERVICES</h2>
    <h3 class="abs h3" style="left:127px;top:1912px;font-size:25px;color:#fff;font-weight:400">BUSINESS CONSULTANCY SERVICE</h3>
    <p class="abs para services-text" style="left:127px;top:1955px;width:475px">At vero eos et accusamus et iusto odio dignissimos ducimus qui blanditiis praesentium voluptatum deleniti atque corrupti quos dolores et quas molestias excepturi sint occaecati cupiditate non provident, similique sunt in culpa qui officia deserunt mollitia animi, id est laborum et dolorum fuga. Et harum quidem rerum facilis est et expedita distinctio.At vero eos et accusamus et iusto odio dignissimos ducimus qui blanditiis praesentium voluptatum deleniti atque corrupti quos dolores et quas molestias excepturi sint occaecati cupiditate non provident, similique sunt in culpa qui officia deserunt mollitia animi, id est laborum et dolorum fuga. Et harum quidem rerum facilis est et expedita distinctio.</p>
    <div class="abs photo" role="img" aria-label="Photo of a client seated on a sofa" style="left:652px;top:1905px;width:380px;height:380px;border-color:var(--blue);background:linear-gradient(135deg,#e5e2dc,#c9bfb3 60%,#a89c91)"></div>
    <svg class="abs" style="left:0;top:2320px" width="1200" height="110" viewBox="0 0 1200 110">
      <path d="M0 60 C400 110 800 80 1200 0 L1200 110 L0 110Z" fill="var(--blue)"/>
      <path d="M0 70 C400 120 800 95 1200 20 L1200 110 L0 110Z" fill="#fff"/>
    </svg>
  </section>

  <section>
    <div class="abs info" style="left:135px;top:2472px">
      <div class="icon"><svg width="44" height="44" viewBox="0 0 24 24" fill="none" stroke="#fff" stroke-width="1.5"><path d="M12 21s-6-6.5-6-11a6 6 0 0 1 12 0c0 4.5-6 11-6 11z"/><circle cx="12" cy="10" r="2.2"/><path d="M5 21h14"/></svg></div>
      418 Larkspur Lane, Elmdale,<br>Ny - 14021
    </div>
    <div class="abs info" style="left:450px;top:2472px">
      <div class="icon"><svg width="44" height="44" viewBox="0 0 24 24" fill="none" stroke="#fff" stroke-width="1.5"><path d="M5 3h4l2 5-2.5 1.5a11 11 0 0 0 6 6L16 13l5 2v4a2 2 0 0 1-2 2A16 16 0 0 1 3 5a2 2 0 0 1 2-2z"/></svg></div>
      Phone:<br>555 014 2290
    </div>
    <div class="abs info" style="left:790px;top:2472px">
      <div class="icon"><svg width="48" height="48" viewBox="0 0 24 24" fill="none" stroke="#fff" stroke-width="1.5"><rect x="3" y="6" width="18" height="12"/><path d="M3 6l9 7 9-7"/></svg></div>
      Email:<br>hello@brightmoorcare.net
    </div>
  </section>

  <section>
    <div class="abs map" role="img" aria-label="Street map showing office locations"></div>
    <svg class="abs" style="left:778px;top:2870px" width="30" height="42" viewBox="0 0 24 34"><path d="M12 34S0 18 0 12a12 12 0 0 1 24 0c0 6-12 22-12 22z" fill="#d23a2c"/><circle cx="12" cy="12" r="4" fill="#8c1f16"/></svg>
    <div class="abs card active" style="top:2712px;height:105px"><p>&#9906; 418 Larkspur Lane, Elmdale, Ny - 14021</p><p>&#9742; 555 014 2290</p><p>&#9993; hello@brightmoorcare.net</p></div>
    <div class="abs card" style="top:2828px;height:105px"><p>&#9906; 62 Orchard Street, Hollowbrook, NY 12740</p><p>&#9742; 555 014 2290</p><p>&#9993; hello@brightmoorcare.net</p></div>
    <div class="abs card" style="top:2944px;height:118px"><p>&#9906; 880 Palmetto Row, Suite 210, Seabright, FL 33980</p><p>&#9742; 555 014 2290</p><p>&#9993; hello@brightmoorcare.net</p></div>
  </section>

  <section>
    <h2 class="abs h2" style="top:3120px">CONTACT US</h2>
    <div class="abs field" style="left:127px;top:3198px;width:463px">&#128100; First Name</div>
    <div class="abs field" style="left:612px;top:3198px;width:463px">&#128100; Last Name</div>
    <div class="abs field" style="left:127px;top:3258px;width:463px">&#9632; Address</div>
    <div class="abs field" style="left:612px;top:3258px;width:463px;height:170px">&#9998; Message :</div>
    <div class="abs field" style="left:127px;top:3318px;width:463px">&#9993; Email Address</div>
    <div class="abs field" style="left:127px;top:3378px;width:463px">&#9742; Phone Number</div>
    <div class="abs btn submit">SUBMIT</div>
  </section>

  <footer>
    <div class="abs footer" role="img" aria-label="Dark photo of a person in a quiet room"></div>
    <svg class="abs" style="left:0;top:3480px" width="1200" height="200" viewBox="0 0 1200 200">
      <path d="M0 0 L1200 0 L1200 10 C900 140 500 170 0 130Z" fill="#fff"/>
      <path d="M0 130 C500 170 900 140 1200 10 L1200 40 C900 170 500 190 0 150Z" fill="var(--blue)"/>
      <path d="M200 150 C600 170 950 120 1200 40 L1200 70 C950 160 600 185 200 150Z" fill="var(--navy)"/>
    </svg>
    <div class="abs fcol" style="left:150px;top:3810px;width:200px">
      <div style="display:flex;align-items:center;gap:7px;font-size:13px;font-weight:700;white-space:nowrap"><span style="width:12px;height:12px;border-radius:50%;background:var(--blue)"></span>Brightmoor Care Partners</div>
      <div style="display:flex;gap:8px;margin:14px 0 0 60px"><span style="width:20px;height:20px;border-radius:50%;border:1px solid #fff"></span><span style="width:20px;height:20px;border-radius:50%;border:1px solid #fff"></span></div>
    </div>
    <div class="abs fcol" style="left:360px;top:3778px;width:240px">
      <h4>CONTACT US</h4>
      <p>&#9906; 418 Larkspur Lane, Elmdale,<br>&nbsp;&nbsp;&nbsp;Ny - 14021</p>
      <p>&#9742; Phone: 555 014 2290</p>
      <p>&#9993; Email: hello@brightmoorcare.net</p>
    </div>
    <div class="abs fcol" style="left:630px;top:3778px;width:250px">
      <h4>SIGN UP FOR NEWSLETTER</h4>
      <p>Want to make an impact? Provide your email</p>
      <div style="margin-top:10px;width:195px;height:26px;background:#fff;color:#999;font-size:10px;padding:6px">Enter email</div>
      <div class="btn" style="margin-top:8px;width:70px;height:22px;font-size:10px">SIGN UP</div>
    </div>
    <div class="abs fcol" style="left:912px;top:3778px;width:150px">
      <h4>QUICK LINKS</h4>
      <p>&bull; Home</p><p>&bull; About Us</p><p>&bull; Our Services</p><p>&bull; Contact Us</p>
    </div>
    <p class="abs copy">Copyrights © 2019 All Rights Reserved | Privacy Policy | Terms and Conditions | Disclaimer | Legal</p>
  </footer>

</div>
</body>
</html>
```